Marketing Flyer for Office Space for Lease

I am looking for a pretty standard and professional real estate flyer listing my property for lease. I am not looking for anything over the top creative, just something very professional looking. The building address is 4817 E. Calloway Avenue, Lauderhill, FL 33319. I included some sample flyers of what other companies use as examples on what I am looking for. Please use the attached Dorvel Holdings Realty logo, but remove the long line after it extends past the words. I also included a Word file that gives you the building information and marketing information. Please use the photos attached in the zipped folder as you see fit.
Updates

Project Deadline Extended
Reason: I am getting updated building measurements next Thursday. I want to be able to give these figures to you to ensure the flyer is final. I will keep making comments on the rest of the designs while I wait for those numbers. Thank you.

Project Deadline Extended
Reason: Just got the floor plans, so I needed to adjust the figures on the flyer. Otherwise I would just have an incorrect flyer.

Target Market(s)

Businesses that would want to lease space in this building.

Industry/Entity Type

Real Estate

Font styles to use
Serif
Sans Serif

Colors

Designer to choose colors to be used in the design.

Requirements
Must have
• Building photo, address, map, and building highlights from the Word file.
Nice to have
• I included the example flyers that I have seen or used in the past. Taking ideas from there could work well.
Should not have
• Crazy big fonts, crazy colors, hard to read fonts, too wild of layout.

```html
<!DOCTYPE html>
<html lang="en">
<head>
<meta charset="utf-8">
<title>Office Space for Lease – 4817 E. Calloway Avenue</title>
<link rel="stylesheet" href="https://fonts.googleapis.com/css2?family=Montserrat:wght@600;700;800;900&family=Open+Sans:wght@400;600;700&display=swap">
<style>
  :root {
    --blue-deep: #0f5d9c;
    --blue-mid: #2b7db8;
    --blue-light: #5aa6d3;
    --ink: #111111;
    --paper: #ffffff;
    --photo-sky: #7fb0dc;
    --photo-wall: #dfe4ea;
    --photo-green: #5d7a3a;
    --map-bg: #e6e4e0;
    --map-edge: #555555;
  }
  * { box-sizing: border-box; margin: 0; padding: 0; }
  html, body {
    width: 927px; height: 1200px; overflow: hidden;
    background: var(--paper);
  }
  .flyer {
    position: relative; width: 927px; height: 1200px;
    background: var(--paper);
    font-family: "Open Sans", Arial, sans-serif;
    color: var(--ink);
  }
  .band {
    background: linear-gradient(90deg, var(--blue-deep) 0%, var(--blue-mid) 40%, var(--blue-light) 55%, var(--blue-mid) 70%, var(--blue-deep) 100%);
    color: var(--paper);
  }
  .title-band {
    position: absolute; left: 0; top: 0; width: 927px; height: 68px;
    display: flex; align-items: center; justify-content: center;
  }
  .title-band h1 {
    font-family: "Montserrat", Arial, sans-serif; font-weight: 900;
    font-size: 46px; letter-spacing: 0.5px;
  }
  .address {
    position: absolute; left: 0; top: 68px; width: 927px; height: 66px;
    display: flex; align-items: center; justify-content: center;
    font-family: "Montserrat", Arial, sans-serif; font-weight: 700; font-size: 29px;
  }
  .photo { position: absolute; }
  .photo-main {
    left: 0; top: 134px; width: 581px; height: 409px;
    background: linear-gradient(180deg, var(--photo-sky) 0%, #b9d3ea 35%, var(--photo-wall) 50%, #9aa2aa 68%, var(--photo-green) 80%, #4a5e2c 100%);
  }
  .photo-aerial {
    left: 588px; top: 271px; width: 335px; height: 237px;
    background: linear-gradient(180deg, #9cc3e6 0%, #6e8f4e 18%, #e6e9ec 40%, #cfd4d8 60%, #4f5358 80%, #3c3f44 100%);
  }
  .photo-entry {
    left: 588px; top: 518px; width: 335px; height: 227px;
    background: linear-gradient(120deg, #f2f3f5 0%, #dde1e5 45%, #a9b0b6 75%, #c6ccd1 100%);
  }
  .area-map {
    position: absolute; left: 588px; top: 754px; width: 335px; height: 329px;
    background: var(--map-bg);
    border: 1px solid var(--map-edge);
  }
  .section-head {
    position: absolute; display: flex; align-items: center;
    font-family: "Montserrat", Arial, sans-serif; font-weight: 800; font-size: 16px;
  }
  .building-head { left: 588px; top: 134px; width: 335px; height: 50px; padding-left: 10px; }
  .marketing-head { left: 0; top: 549px; width: 581px; height: 51px; padding-left: 38px; }
  .building-facts {
    position: absolute; left: 606px; top: 204px; list-style: none; font-size: 14.5px;
  }
  .building-facts li { position: relative; padding-left: 18px; height: 28px; }
  .building-facts strong { font-family: "Montserrat", Arial, sans-serif; font-weight: 700; font-size: 15px; }
  .features {
    position: absolute; left: 44px; top: 640px; width: 530px; list-style: none;
    font-size: 15px; line-height: 20px;
  }
  .features > li { position: relative; padding-left: 25px; margin-bottom: 6px; }
  .sub-features { list-style: none; margin-top: 5px; margin-left: 40px; }
  .sub-features li { position: relative; padding-left: 20px; margin-bottom: 3px; }
  .building-facts li::before, .features li::before {
    content: ""; position: absolute; left: 0; top: 5px;
    border-left: 10px solid var(--ink);
    border-top: 5.5px solid transparent; border-bottom: 5.5px solid transparent;
  }
  .contact-band {
    position: absolute; left: 0; top: 1089px; width: 927px; height: 111px;
    display: flex; flex-direction: column; align-items: center; justify-content: center;
    font-family: "Montserrat", Arial, sans-serif; font-weight: 700; font-size: 27px; line-height: 1.3;
  }
  .contact-band .phone { font-size: 35px; font-weight: 800; }
</style>
</head>
<body>
<main class="flyer">
  <header class="title-band band"><h1>OFFICE SPACE FOR LEASE</h1></header>
  <div class="address">4817 E. CALLOWAY AVENUE, LAUDERHILL, FL 33319</div>

  <div class="photo photo-main" role="img" aria-label="Front view of the three-story white office building with landscaped entrance and monument sign"></div>

  <div class="section-head building-head band">BUILDING INFORMATION:</div>
  <ul class="building-facts">
    <li>Total Building Size: <strong>38,485 SF</strong></li>
    <li>Vacant Space: <strong>26,878 SF</strong></li>
  </ul>
  <div class="photo photo-aerial" role="img" aria-label="Aerial view of the building and its parking lot"></div>
  <div class="photo photo-entry" role="img" aria-label="Close view of the building corner with street number"></div>
  <div class="area-map" role="img" aria-label="Street map locating the office space for lease at 4817 E. Calloway Avenue"></div>

  <div class="section-head marketing-head band">MARKETING INFORMATION AND FEATURES:</div>
  <ul class="features">
    <li>New landlord recently purchased the building and is moving into the 3rd floor.</li>
    <li>Can accommodate a tenant up to 26,000 SF</li>
    <li>Monument signage available</li>
    <li>Located right on Calloway Avenue and a few blocks away from busiest intersection in all of Broward County, Calloway Ave and 441.</li>
    <li>Parking ratio over 5 per 1,000 SF including secured, private parking in rear of building.</li>
    <li>Building undergoing upgrades both exterior and interior:
      <ul class="sub-features">
        <li>New Landscaping</li>
        <li>New exterior paint</li>
        <li>Upgraded common area hallways</li>
        <li>Upgraded common area bathrooms</li>
        <li>New security card access system for building</li>
      </ul>
    </li>
    <li>Negotiable tenant improvement allowances.</li>
    <li>Competitive rental rates.</li>
    <li>On-site management.</li>
    <li>Can accommodate professional or medical offices.</li>
  </ul>

  <footer class="contact-band band">
    <div>Call Marcus Delane at <span class="phone">561-555-0143</span> or</div>
    <div>email marcus@dorvelholdings.com</div>
  </footer>
</main>
</body>
</html>
```